Vantrell Law Letterhead

We need a new letterhead design for a Law Firm. The address for the law firm is 4817 Larkspur Boulevard, Suite 250, Houston, Texas 77342. Phone Number: 832-619-3057; Fax Number: 832-407-1694. The logo is uploaded to the project.

```html
<!DOCTYPE html>
<html lang="en">
<head>
<meta charset="utf-8">
<title>Vantrell Law Letterhead</title>
<link rel="stylesheet" href="https://fonts.googleapis.com/css2?family=Libre+Caslon+Text&family=Roboto:wght@400;500&display=swap">
<style>
  :root {
    --backdrop: #e1e1e1;
    --paper: #ffffff;
    --firm-red: #961a1e;
    --accent-red: #d81f26;
    --firm-navy: #1b2f5e;
    --ink: #1a1a1a;
  }
  * { margin: 0; padding: 0; box-sizing: border-box; }
  html, body {
    width: 1080px;
    height: 1200px;
    overflow: hidden;
    background: var(--backdrop);
  }
  .letterhead {
    position: absolute;
    left: 116px;
    top: 0;
    width: 848px;
    height: 1200px;
    background: var(--paper);
    overflow: hidden;
  }
  .letterhead-curves {
    position: absolute;
    inset: 0;
    width: 100%;
    height: 100%;
  }
  .curve-top { fill: var(--firm-red); }
  .curve-bottom { fill: var(--firm-navy); }

  .masthead {
    position: absolute;
    left: 0;
    right: 0;
    top: 152px;
    text-align: center;
  }
  .firm-name {
    font-family: "Libre Caslon Text", serif;
    font-size: 46px;
    font-weight: 400;
    color: var(--firm-navy);
    line-height: 1;
  }
  .tagline {
    margin-top: 26px;
    font-family: "Libre Caslon Text", serif;
    font-size: 9px;
    letter-spacing: 1.6px;
    color: var(--accent-red);
    line-height: 1;
  }

  .footer-rule {
    position: absolute;
    left: 125px;
    width: 599px;
    top: 1050px;
    height: 1px;
    background: var(--firm-red);
  }
  .footer-divider {
    position: absolute;
    left: 392px;
    top: 1069px;
    width: 2px;
    height: 73px;
    background: var(--firm-navy);
  }
  .footer-block {
    position: absolute;
    font-family: "Roboto", sans-serif;
    color: var(--ink);
  }
  .footer-heading {
    font-size: 14px;
    font-weight: 500;
    line-height: 1;
  }
  .footer-lines {
    margin-top: 13px;
    margin-left: 32px;
    font-size: 12.5px;
    line-height: 17px;
  }
  .contact-block { left: 185px; top: 1076px; }
  .address-block { left: 423px; top: 1076px; }
  .address-block .footer-heading { font-size: 13px; }
  .contact-row { display: flex; }
  .contact-label { width: 50px; }
</style>
</head>
<body>
  <main class="letterhead">
    <svg class="letterhead-curves" viewBox="0 0 986 1396" preserveAspectRatio="none" aria-hidden="true">
      <path class="curve-top" d="M0 257 C30 120 160 60 400 25 C600 5 800 2 986 0 H0 Z"/>
      <path class="curve-bottom" d="M986 1140 C960 1260 880 1330 600 1368 C400 1390 200 1392 0 1396 H986 Z"/>
    </svg>

    <header class="masthead">
      <h1 class="firm-name">Vantrell Law</h1>
      <p class="tagline">STEADY COUNSEL WHEN IT MATTERS MOST</p>
    </header>

    <div class="footer-rule"></div>

    <section class="footer-block contact-block">
      <h2 class="footer-heading">Contact Information</h2>
      <div class="footer-lines">
        <div class="contact-row"><span class="contact-label">Phone:</span><span>832-619-3057</span></div>
        <div class="contact-row"><span class="contact-label">Fax:</span><span>832-407-1694</span></div>
      </div>
    </section>

    <div class="footer-divider"></div>

    <section class="footer-block address-block">
      <h2 class="footer-heading">Physical Address</h2>
      <div class="footer-lines">
        <div>4817 Larkspur Boulevard,</div>
        <div>Suite 250, Houston Texas 77342</div>
      </div>
    </section>
  </main>
</body>
</html>
```